Brindlewick Appliances

we want our logo to be the full front of the card listing our address email and phone and for it to state at our address is a showroom. back of card list of appliances i listed below. Also want the KTR Logo, Chatterleaf Icon and Pixelmoor Icon on card

Industry/Entity Type

Outdoor appliances

Contact Information for Business Card

Front of card to show our logo, address and state under logo showroom under the addresslist of appliances we sell on back of card - Orvo, TPK, Zelt, Kesta, Marvik, Holtby, Stonewick, Parvello, Rutherby, Blue Harrow, Lindell Crane, Coastal Brenn, Quiet Ravens

Requirements
Must have
• Our email (Info@Brindlewickqz.com) phone (555-203-6184), address,(87 Tolliver Lane Mineola, NY 11501) KTR Icon, CL Icon and PM Icon, our list of appliances
Nice to have
• Logo on front as big as can be and appliances listed on back of card we carry

```html
<!DOCTYPE html>
<html lang="en">
<head>
<meta charset="utf-8">
<title>Brindlewick Appliances – Business Card</title>
<link href="https://fonts.googleapis.com/css2?family=Poppins:wght@400;500;600;700&display=swap" rel="stylesheet">
<style>
  :root {
    --bg: #e4e4e4;
    --paper: #f4f4f4;
    --brand-red: #e8222e;
    --brand-blue: #2453ad;
    --ink: #1c1c1c;
    --white: #ffffff;
    --white-soft: rgba(255,255,255,.82);
  }
  * { margin: 0; padding: 0; box-sizing: border-box; }
  html, body {
    width: 1200px; height: 900px; overflow: hidden;
    background: var(--bg);
    font-family: "Poppins", sans-serif;
  }
  .stage { position: relative; width: 1200px; height: 900px; }
  .card {
    position: absolute; left: 320px;
    width: 560px; height: 320px;
    background: var(--paper);
    border-radius: 6px;
    overflow: hidden;
    box-shadow: 0 10px 28px rgba(0,0,0,.18);
  }
  .card--back { top: 100px; }
  .card--front { top: 480px; }

  /* Back side */
  .back-logo {
    position: absolute; top: 40px; left: 0; right: 0;
    display: flex; justify-content: center; align-items: center; gap: 10px;
    font-weight: 700; font-size: 28px; color: var(--brand-red);
  }
  .logo-mark { width: 18px; height: 18px; background: var(--brand-blue); }
  .brand-list {
    position: absolute; top: 112px; left: 40px; right: 40px;
    text-align: center; color: var(--ink);
  }
  .brand-list__title { font-weight: 600; font-size: 15px; margin-bottom: 4px; }
  .brand-list__items { font-weight: 400; font-size: 15px; line-height: 1.4; }
  .back-band {
    position: absolute; left: 0; right: 0; bottom: 0; height: 76px;
    display: flex;
  }
  .back-band__red { flex: 1; background: var(--brand-red); }
  .back-band__blue { flex: 1; background: var(--brand-blue); }

  /* Front side */
  .front-top { position: absolute; top: 0; left: 0; right: 0; height: 112px; display: flex; }
  .front-top__white { width: 58%; background: var(--paper); }
  .front-top__red { flex: 1; background: var(--brand-red); }
  .front-logo {
    position: absolute; top: 36px; left: 30px;
    display: flex; align-items: center; gap: 8px;
    font-weight: 700; font-size: 20px; color: var(--brand-red);
  }
  .front-logo .logo-mark { width: 14px; height: 14px; }
  .front-panel {
    position: absolute; top: 112px; left: 0; right: 0; bottom: 0;
    background: var(--brand-blue); color: var(--white);
  }
  .person {
    position: absolute; top: 38px; left: 24px; width: 196px; text-align: right;
  }
  .person__name { font-weight: 600; font-size: 32px; line-height: 1; letter-spacing: .5px; white-space: nowrap; }
  .person__role { font-weight: 400; font-size: 20px; line-height: 1.3; letter-spacing: 1px; }
  .divider {
    position: absolute; top: 20px; left: 236px; width: 2px; height: 112px;
    background: var(--white);
  }
  .contact-list {
    position: absolute; top: 16px; left: 254px; right: 16px; list-style: none;
    font-size: 13px; font-weight: 400; line-height: 1.3;
  }
  .contact-list li { display: flex; align-items: flex-start; gap: 10px; margin-bottom: 10px; }
  .contact-icon {
    flex: none; width: 20px; height: 20px; border-radius: 50%;
    background: var(--white); display: flex; align-items: center; justify-content: center;
  }
  .contact-icon svg { width: 12px; height: 12px; }
  .contact-text { padding-top: 1px; white-space: nowrap; }
  .contact-note { display: block; font-size: 12px; font-weight: 600; color: var(--white-soft); letter-spacing: .6px; }
  .social-row {
    position: absolute; right: 24px; bottom: 18px;
    display: flex; align-items: center; gap: 12px;
    font-size: 11px; font-weight: 600;
  }
  .social-row .badge { width: 16px; height: 22px; background: var(--white); border-radius: 2px; }
  .social-item { display: flex; align-items: center; gap: 4px; }
  .social-item .dot { width: 10px; height: 10px; border-radius: 50%; background: var(--white); }
</style>
</head>
<body>
<main class="stage">

  <section class="card card--back" aria-label="Card back">
    <div class="back-logo"><span class="logo-mark"></span>Brindlewick Appliances</div>
    <div class="brand-list">
      <p class="brand-list__title">WE SELL</p>
      <p class="brand-list__items">Orvo, TPK, Zelt, Kesta, Marvik, Holtby, Stonewick,<br>Parvello, Rutherby, Blue Harrow, Lindell Crane,<br>Coastal Brenn, Quiet Ravens</p>
    </div>
    <div class="back-band">
      <div class="back-band__red"></div>
      <div class="back-band__blue"></div>
    </div>
  </section>

  <section class="card card--front" aria-label="Card front">
    <div class="front-top">
      <div class="front-top__white"></div>
      <div class="front-top__red"></div>
    </div>
    <div class="front-logo"><span class="logo-mark"></span>Brindlewick Appliances</div>
    <div class="front-panel">
      <div class="person">
        <p class="person__name">JOHN DOE</p>
        <p class="person__role">FOUNDER</p>
      </div>
      <div class="divider"></div>
      <ul class="contact-list">
        <li>
          <span class="contact-icon"><svg viewBox="0 0 24 24"><path fill="#2453ad" d="M6.6 10.8a15.1 15.1 0 0 0 6.6 6.6l2.2-2.2a1 1 0 0 1 1-.25 11.4 11.4 0 0 0 3.6.57 1 1 0 0 1 1 1V20a1 1 0 0 1-1 1A17 17 0 0 1 3 4a1 1 0 0 1 1-1h3.5a1 1 0 0 1 1 1c0 1.25.2 2.45.57 3.57a1 1 0 0 1-.25 1z"/></svg></span>
          <span class="contact-text">555-203-6184</span>
        </li>
        <li>
          <span class="contact-icon"><svg viewBox="0 0 24 24"><rect x="3" y="5" width="18" height="14" rx="1.5" fill="none" stroke="#2453ad" stroke-width="2.2"/><path d="M3 6l9 7 9-7" fill="none" stroke="#2453ad" stroke-width="2.2"/></svg></span>
          <span class="contact-text">Info@Brindlewickqz.com</span>
        </li>
        <li>
          <span class="contact-icon"><svg viewBox="0 0 24 24"><path fill="#2453ad" d="M12 2a7 7 0 0 0-7 7c0 5.2 7 13 7 13s7-7.8 7-13a7 7 0 0 0-7-7zm0 9.5A2.5 2.5 0 1 1 12 6.5a2.5 2.5 0 0 1 0 5z"/></svg></span>
          <span class="contact-text">87 Tolliver Lane<br>Mineola, NY 11501<span class="contact-note">SHOWROOM</span></span>
        </li>
      </ul>
      <div class="social-row">
        <span class="badge" role="img" aria-label="KTR accreditation badge"></span>
        <span class="social-item"><span class="dot"></span>CL</span>
        <span class="social-item"><span class="dot"></span>PM</span>
      </div>
    </div>
  </section>

</main>
</body>
</html>
```